Advertisement for tellmark Ad

We are looking to copy a mailer style design that would normally be sent out to a mailbox. However we have decided to simply use it and run an add on Tellmark. please check photo sizes for tellmark to make sure your design will work.

also please try to use the colors from our website: riverbendhollow@mailnest.com

we want the same layout as the ad we sent in the files, with different photos and color scheme.

Target Market(s)

dog owners with busy schedules

Font styles to use
Sans Serif

Colors

Designer to choose only greyscale colors for use in the design.

```html
<!DOCTYPE html>
<html lang="en">
<head>
<meta charset="utf-8">
<title>Riverbend Hollow Canine Center – Daycare Ad</title>
<link rel="stylesheet" href="https://fonts.googleapis.com/css2?family=Open+Sans:wdth,wght@75,700&family=Arimo:wght@400&display=swap">
<style>
  :root {
    --accent: #c4c4c4;
    --accent-strong: #d9d9d9;
    --panel: #474747;
    --band-top: #3b3b3b;
    --band-bottom: #1c1c1c;
    --offer-title: #e4e4e4;
    --white: #ffffff;
    --ink: #1a1a1a;
    --photo-light: #dcdcdc;
    --photo-mid: #a9a9a9;
    --photo-dark: #7a7a7a;
  }
  html, body {
    margin: 0;
    padding: 0;
    overflow: hidden;
    background: #ffffff;
  }
  .ad {
    position: relative;
    width: 1200px;
    height: 457px;
    overflow: hidden;
    font-family: "Arimo", Arial, sans-serif;
  }
  .hero-photo {
    position: absolute;
    left: 0;
    top: 0;
    width: 680px;
    height: 301px;
    background:
      radial-gradient(ellipse at 58% 50%, var(--photo-light) 0%, var(--photo-mid) 50%, transparent 80%),
      linear-gradient(180deg, var(--photo-dark) 0%, var(--photo-mid) 45%, #bdbdbd 80%, #cfcfcf 100%);
  }
  .shapes {
    position: absolute;
    left: 0;
    top: 0;
  }
  .headline {
    position: absolute;
    left: 740px;
    top: 13px;
    margin: 0;
    font-family: "Open Sans", "Arial Narrow", sans-serif;
    font-stretch: 75%;
    font-weight: 700;
    font-size: 44px;
    line-height: 40px;
    letter-spacing: 2.3px;
    color: var(--accent-strong);
  }
  .perks {
    position: absolute;
    left: 741px;
    top: 101px;
    margin: 0;
    padding: 0;
    list-style: none;
    color: var(--white);
    font-size: 16.5px;
    line-height: 18px;
    letter-spacing: 0.3px;
  }
  .perks .aside {
    font-size: 13.5px;
    margin-top: 2px;
  }
  .contact {
    position: absolute;
    left: 741px;
    top: 217px;
    margin: 0;
    color: var(--white);
    font-size: 12px;
    line-height: 14.7px;
    letter-spacing: 0.5px;
    font-style: normal;
  }
  .brand {
    position: absolute;
    left: 18px;
    top: 262px;
    display: flex;
    align-items: center;
    gap: 8px;
    font-size: 13px;
    color: var(--ink);
    letter-spacing: 0.5px;
  }
  .brand-mark {
    width: 14px;
    height: 14px;
    background: var(--ink);
  }
  .offer {
    position: absolute;
    top: 324px;
    width: 300px;
    text-align: center;
    font-family: "Open Sans", "Arial Narrow", sans-serif;
    font-stretch: 75%;
    font-weight: 700;
  }
  .offer-title {
    margin: 0;
    font-size: 29px;
    line-height: 27px;
    letter-spacing: 1.2px;
    color: var(--offer-title);
  }
  .offer-expiry {
    margin: 3px 0 0;
    font-size: 17px;
    letter-spacing: 1px;
    color: var(--white);
  }
  .offer--daycare { left: 32px; }
  .offer--bath { left: 470px; }
  .offer--groom { left: 870px; }
</style>
</head>
<body>
<div class="ad">
  <div class="hero-photo" role="img" aria-label="Photo of puppies playing together on the grass"></div>

  <svg class="shapes" width="1200" height="457" viewBox="0 0 1200 457" aria-hidden="true">
    <defs>
      <linearGradient id="bandShade" x1="0" y1="0" x2="0" y2="1">
        <stop offset="0" stop-color="#3b3b3b"/>
        <stop offset="1" stop-color="#1c1c1c"/>
      </linearGradient>
    </defs>
    <polygon points="563,0 1200,0 1200,301 660,301" fill="#c4c4c4"/>
    <polygon points="605,0 1200,0 1200,268 671,295" fill="#ffffff"/>
    <polygon points="608,0 1200,0 1200,264 672,289" fill="#474747"/>
    <rect x="0" y="301" width="1200" height="156" fill="url(#bandShade)"/>
    <line x1="451" y1="320" x2="385" y2="437" stroke="#c4c4c4" stroke-width="5"/>
    <line x1="877" y1="320" x2="811" y2="437" stroke="#c4c4c4" stroke-width="5"/>
  </svg>

  <div class="brand">
    <span class="brand-mark"></span>
    <span>Riverbend Hollow Canine Center</span>
  </div>

  <h1 class="headline">NOT YOUR TYPICAL<br>DOG DAYCARE</h1>

  <ul class="perks">
    <li>SAFE, OPEN-PLAY DAYCARE</li>
    <li>EXCERCISE &amp; EDUCATION</li>
    <li>FUN FILLED DAYS WITH</li>
    <li>THEIR BEEF</li>
    <li class="aside">(BEST FURRY FRIEND FOREVER)</li>
  </ul>

  <address class="contact">
    Riverbend Hollow Canine Center<br>
    418 Willow Bend Road Maple Falls IA<br>
    555-014-2286
  </address>

  <div class="offer offer--daycare">
    <p class="offer-title">FREE FIRST DAY<br>OF DAYCARE!*</p>
    <p class="offer-expiry">use by 8/31/20</p>
  </div>
  <div class="offer offer--bath">
    <p class="offer-title">ONE FREE<br>BATH!*</p>
    <p class="offer-expiry">use by 8/31/20</p>
  </div>
  <div class="offer offer--groom">
    <p class="offer-title">$20 OFF<br>FIRST GROOM</p>
    <p class="offer-expiry">use by 8/31/20</p>
  </div>
</div>
</body>
</html>
```